Kinetra Limbworks tri-fold brochure

Create a three panel brochure, front and back, for company named Kinetra Limbworks. It should have a modern and high-tech feel. It should appeal to not only patients but also physicians, physical therapists, and other medical personnel. Stock photos are fine but our logo must be included. You can also use the pictures from our website which is velmorastride.example or kinetralimb.example. They are the same website but we are rebranding for velmora stride to kinetra limbworks. Should also state "Hablamos Espanol" on the front of the brochure somewhere.
Updates

I have added pics and updated my profile. Sorry for the delay Added Monday, November 28, 2016

Target Market(s)

Amputees, Physicians, and Therapists

Industry/Entity Type

It Company

Requirements
Must have
• Kinetra Limbworks logo
• Office Locations:
• 4872 Wrenfield Drive, Ste 304
• Memphis, TN 38119
• Phone (555) 214-8830
• Fax (555) 214-8867
• 27904 Caskbridge Court, Ste B
• Houston, TX 77082
• Phone: (555) 630-4195
• Fax: (555)630-4172
• 8467 Quillory Street, Ste 200
• Arlington, TX 76015
• Phone: (555) 781-3046
• Fax: (555) 781-3019
• Hablamos EspaƱol
Nice to have
• Emphasis on patient care

```html
<!DOCTYPE html>
<html lang="en">
<head>
<meta charset="utf-8">
<title>Kinetra Limbworks – Tri-fold Brochure</title>
<link rel="stylesheet" href="https://fonts.googleapis.com/css2?family=Open+Sans:wght@400;600;700&display=swap">
<style>
  :root{
    --blue:#0b63d6;
    --blue-light:#1a86ee;
    --navy:#0e1f6e;
    --navy-light:#1c3494;
    --red:#d8161e;
    --ink-red:#b3121c;
    --ink-blue:#1b3a8f;
    --paper:#ffffff;
    --paper-shade:#eef0f3;
    --canvas:#e6e7e9;
    --text-dark:#3a3f4a;
  }
  *{box-sizing:border-box;margin:0;padding:0}
  html,body{width:880px;height:1200px;overflow:hidden}
  body{background:var(--canvas);font-family:"Open Sans",Arial,sans-serif;position:relative}
  .spread{position:absolute;left:20px;width:840px;height:560px;display:flex;box-shadow:0 6px 18px rgba(0,0,0,.18)}
  .spread--outside{top:20px}
  .spread--inside{top:620px}
  .panel{position:relative;width:280px;height:560px;overflow:hidden;background:var(--paper)}
  .panel + .panel{border-left:1px solid rgba(0,0,0,.06)}
  .wave{position:absolute;left:0;top:0;width:280px;height:560px}
  .photo{position:absolute}

  /* Outside – mission */
  .mission{background:linear-gradient(160deg,var(--blue-light),var(--blue) 70%)}
  .mission__body{position:absolute;left:26px;top:34px;right:22px;color:#fff}
  .mission h2{font-size:19px;font-weight:700;margin-bottom:10px}
  .mission p{font-size:10.2px;line-height:1.45;margin-bottom:9px}
  .mission .photo{left:70px;top:340px;width:170px;height:190px;border-radius:20px 20px 50px 50px;
    background:linear-gradient(180deg,#2a2d33,#4a4d55 55%,#c4432d)}

  /* Outside – offices */
  .offices{background:linear-gradient(180deg,var(--navy-light),var(--navy))}
  .offices__title{position:absolute;left:40px;top:30px;width:200px;height:30px;border:1px solid rgba(255,255,255,.45);
    border-radius:15px;color:#fff;font-size:14px;text-align:center;line-height:28px}
  .office{position:absolute;left:0;width:280px;text-align:center;color:#dfe6ff;font-size:9px;line-height:1.5}
  .office .pin{display:block;margin:0 auto 4px}
  .offices .photo{left:30px;top:340px;width:220px;height:70px;border-radius:40px;
    background:radial-gradient(ellipse at 60% 50%,#cfe3ff 0,#3e66c9 30%,rgba(14,31,110,0) 70%)}
  .social{position:absolute;top:478px;left:0;width:280px;display:flex;justify-content:center;gap:8px}
  .social span{width:16px;height:16px;border-radius:50%;background:var(--ink-blue)}
  .web{position:absolute;font-size:11px;color:var(--text-dark);display:flex;align-items:center;gap:6px}
  .web i{width:8px;height:8px;border-radius:50%;border:2px solid var(--red);display:inline-block}
  .offices .web{left:0;width:280px;justify-content:center;top:506px}

  /* Outside – cover */
  .cover .photo{left:0;top:0;width:280px;height:380px;
    background:linear-gradient(170deg,#2d5aa8,#1b3f86 45%,#6a7fa0 80%,#a58f7d)}
  .brand{position:absolute;left:60px;top:440px;display:flex;align-items:center;gap:8px}
  .brand__mark{width:18px;height:18px;border-radius:50%;background:var(--red)}
  .brand__name{font-size:19px;font-weight:700;color:var(--ink-red)}
  .cover .web{left:60px;top:488px}
  .cover__language{position:absolute;left:60px;top:512px;font-size:12px;font-weight:600;color:var(--ink-blue)}

  /* Inside – services */
  .services{background:linear-gradient(165deg,var(--blue-light),var(--blue) 70%)}
  .services__body{position:absolute;left:26px;top:30px;right:16px;color:#fff}
  .services h2{font-size:19px;font-weight:700;margin-bottom:14px}
  .feature{display:flex;gap:8px;margin-bottom:12px}
  .feature svg{flex:none;margin-top:3px}
  .feature b{display:block;font-size:12px;font-weight:700;line-height:1.4}
  .feature span{display:block;font-size:11px;line-height:1.4}
  .contact{position:absolute;left:40px;top:480px;font-size:13px;color:var(--text-dark);line-height:1.9}
  .contact div{display:flex;align-items:center;gap:8px}

  /* Inside – list panels */
  .heading-red{color:var(--ink-red);font-weight:700;font-size:14px;line-height:1.3}
  .range{position:absolute;left:22px;top:34px;right:20px}
  .range p{margin-top:8px;font-size:10px;line-height:1.5;color:var(--ink-blue)}
  .range .photo{left:-22px;top:210px;width:280px;height:350px;background:linear-gradient(180deg,#dfe3ea,#3a4f7f 60%,#26385f)}
  .outcome{position:absolute;left:22px;top:34px;right:18px}
  .outcome .heading-red{font-weight:400;font-size:15px}
  .outcome ul{list-style:none;margin-top:12px}
  .outcome li{display:flex;gap:7px;font-size:10.5px;color:var(--text-dark);margin-bottom:5px;line-height:1.35}
  .outcome li svg{flex:none;margin-top:2px}
  .outcome-photo{left:0;top:205px;width:280px;height:270px;background:linear-gradient(180deg,#f2f2f2,#e9c77a 55%,#c99a4a)}
  .inside-web{left:80px;top:510px}
</style>
</head>
<body>

<section class="spread spread--outside">
  <article class="panel mission">
    <div class="mission__body">
      <h2>Our Mission</h2>
      <p>To utilize education, experience and dedication in an effort to provide the most comprehensive prosthetic and orthotic care available.</p>
      <p>Our professionals are fully trained to evaluate, fabricate and fit every type of artificial limb and brace for the adult and pediatric population. We offer support and understanding as we counsel our patients in a safe and effective utilization of our devices. No two patients are the same at Kinetra Limbworks.</p>
      <p>We pride ourselves in treating every patient as an individual with dignity and respect.</p>
      <p>We guarantee high quality and fast turnaround on all our products.</p>
    </div>
    <svg class="wave" viewBox="0 0 280 560" preserveAspectRatio="none" aria-hidden="true">
      <path d="M0,420 Q140,445 280,470 L280,560 L0,560Z" fill="var(--paper-shade)"/>
      <path d="M0,414 Q140,439 280,464" stroke="var(--red)" stroke-width="4" fill="none"/>
      <path d="M0,420 Q140,445 280,470" stroke="var(--paper)" stroke-width="2" fill="none"/>
    </svg>
    <div class="photo" role="img" aria-label="Product photo of decorated prosthetic sockets with a foot component"></div>
  </article>

  <article class="panel offices">
    <div class="offices__title">Office Locations:</div>
    <div class="office" style="top:78px">
      <svg class="pin" width="10" height="12" viewBox="0 0 10 12"><path d="M5 0a4 4 0 0 1 4 4c0 3-4 8-4 8S1 7 1 4a4 4 0 0 1 4-4z" fill="#fff"/><circle cx="5" cy="4" r="1.5" fill="var(--navy)"/></svg>
      4872 Wrenfield Drive, Ste 304<br>Memphis, TN 38119<br>Phone (555) 214-8830<br>Fax (555) 214-8867
    </div>
    <div class="office" style="top:166px">
      <svg class="pin" width="10" height="12" viewBox="0 0 10 12"><path d="M5 0a4 4 0 0 1 4 4c0 3-4 8-4 8S1 7 1 4a4 4 0 0 1 4-4z" fill="#fff"/><circle cx="5" cy="4" r="1.5" fill="var(--navy)"/></svg>
      27904 Caskbridge Court, Ste B<br>Houston, TX 77082<br>Phone: (555) 630-4195<br>Fax: (555)630-4172
    </div>
    <div class="office" style="top:254px">
      <svg class="pin" width="10" height="12" viewBox="0 0 10 12"><path d="M5 0a4 4 0 0 1 4 4c0 3-4 8-4 8S1 7 1 4a4 4 0 0 1 4-4z" fill="#fff"/><circle cx="5" cy="4" r="1.5" fill="var(--navy)"/></svg>
      8467 Quillory Street, Ste 200<br>Arlington, TX 76015<br>Phone: (555) 781-3046<br>Fax: (555) 781-3019
    </div>
    <div class="photo" role="img" aria-label="Illustration of a robotic hand reaching toward a human hand with a bright glow"></div>
    <svg class="wave" viewBox="0 0 280 560" preserveAspectRatio="none" aria-hidden="true">
      <path d="M0,450 Q140,440 280,400 L280,560 L0,560Z" fill="var(--paper-shade)"/>
      <path d="M0,440 Q140,430 280,390" stroke="var(--red)" stroke-width="4" fill="none"/>
      <path d="M0,446 Q140,436 280,396" stroke="var(--paper)" stroke-width="3" fill="none"/>
      <path d="M0,451 Q140,441 280,401" stroke="var(--blue)" stroke-width="4" fill="none"/>
    </svg>
    <div class="social"><span></span><span></span><span></span><span></span></div>
    <div class="web"><i></i>www.kinetralimb.example</div>
  </article>

  <article class="panel cover">
    <div class="photo" role="img" aria-label="Photo of a sprinter with a running blade prosthesis on a stadium track"></div>
    <svg class="wave" viewBox="0 0 280 560" preserveAspectRatio="none" aria-hidden="true">
      <path d="M0,395 Q150,370 280,310 L280,560 L0,560Z" fill="var(--paper-shade)"/>
      <path d="M0,380 Q150,355 280,295" stroke="var(--red)" stroke-width="6" fill="none"/>
      <path d="M0,387 Q150,362 280,302" stroke="var(--paper)" stroke-width="4" fill="none"/>
      <path d="M0,394 Q150,369 280,309" stroke="var(--blue)" stroke-width="6" fill="none"/>
    </svg>
    <div class="brand"><span class="brand__mark"></span><span class="brand__name">Kinetra Limbworks</span></div>
    <div class="web"><i></i>www.kinetralimb.example</div>
    <div class="cover__language" lang="es">Hablamos Español</div>
  </article>
</section>

<section class="spread spread--inside">
  <article class="panel services">
    <div class="services__body">
      <h2>Our Services</h2>
      <div class="feature"><svg width="12" height="12" viewBox="0 0 12 12"><path d="M2 11V6a4 4 0 0 1 8 0M7 3l3 3 2-3" stroke="#fff" stroke-width="1.6" fill="none"/></svg><div><b>First Class Patient Care -</b><span>We always put patient needs and safety first.</span></div></div>
      <div class="feature"><svg width="12" height="12" viewBox="0 0 12 12"><path d="M2 11V6a4 4 0 0 1 8 0M7 3l3 3 2-3" stroke="#fff" stroke-width="1.6" fill="none"/></svg><div><b>High End Technology –</b><span>We are always current on the latest socket and component technology</span></div></div>
      <div class="feature"><svg width="12" height="12" viewBox="0 0 12 12"><path d="M2 11V6a4 4 0 0 1 8 0M7 3l3 3 2-3" stroke="#fff" stroke-width="1.6" fill="none"/></svg><div><b>Experience -</b><span>15 years technical &amp; practitioner experience</span></div></div>
      <div class="feature"><svg width="12" height="12" viewBox="0 0 12 12"><path d="M2 11V6a4 4 0 0 1 8 0M7 3l3 3 2-3" stroke="#fff" stroke-width="1.6" fill="none"/></svg><div><b>Fast Turnaround –</b><span>Same day prosthetic service available</span></div></div>
      <div class="feature"><svg width="12" height="12" viewBox="0 0 12 12"><path d="M2 11V6a4 4 0 0 1 8 0M7 3l3 3 2-3" stroke="#fff" stroke-width="1.6" fill="none"/></svg><div><b>Firm Belief In Teamwork –</b><span>We love to work with the patient, rehabilitative staff and physicians to achieve the patient's goal.</span></div></div>
    </div>
    <svg class="wave" viewBox="0 0 280 560" preserveAspectRatio="none" aria-hidden="true">
      <path d="M0,462 Q140,455 280,470 L280,560 L0,560Z" fill="var(--paper-shade)"/>
      <path d="M0,452 Q140,445 280,460" stroke="var(--red)" stroke-width="3" fill="none"/>
      <path d="M0,457 Q140,450 280,465" stroke="var(--paper)" stroke-width="2" fill="none"/>
      <path d="M0,462 Q140,455 280,470" stroke="var(--blue)" stroke-width="3" fill="none"/>
    </svg>
    <div class="contact">
      <div><svg width="12" height="12" viewBox="0 0 12 12"><circle cx="6" cy="6" r="5.2" stroke="var(--red)" stroke-width="1.4" fill="none"/><path d="M4 3.5l1 1.5-.6.8a4 4 0 0 0 1.8 1.8l.8-.6 1.5 1-.6 1A5 5 0 0 1 3 4.1z" fill="var(--red)"/></svg>(555) 214-8800</div>
      <div><svg width="12" height="10" viewBox="0 0 12 10"><rect x="1" y="1" width="10" height="8" stroke="var(--red)" stroke-width="1.3" fill="none"/><path d="M1 1l5 4 5-4" stroke="var(--red)" stroke-width="1.3" fill="none"/></svg>info@kinetralimb.example</div>
    </div>
  </article>

  <article class="panel">
    <div class="range">
      <div class="heading-red">Prosthetic Services Include<br>but are not limited to:</div>
      <p>AK Prosthesis (Transfemoral), BK Prosthesis (Transtibial), AE Prosthesis (Transhumeral), BE Prosthesis (Transradial), Partial Foot Prosthesis, Hip Disarticulation Prosthesis, Shoulder Disarticulation Prosthesis, Micro-Processor Knees, Myo-electric Components, and anything you can think of related to the absence of a limb.</p>
      <div class="photo" role="img" aria-label="Photo of a practitioner at a laptop fitting a prosthetic arm on a patient"></div>
    </div>
    <svg class="wave" viewBox="0 0 280 560" preserveAspectRatio="none" aria-hidden="true">
      <path d="M0,560 Q150,540 280,480 L280,560Z" fill="var(--paper-shade)"/>
      <path d="M0,546 Q150,526 280,466" stroke="var(--red)" stroke-width="5" fill="none"/>
      <path d="M0,552 Q150,532 280,472" stroke="var(--paper)" stroke-width="3" fill="none"/>
      <path d="M0,558 Q150,538 280,478" stroke="var(--blue)" stroke-width="5" fill="none"/>
    </svg>
  </article>

  <article class="panel">
    <div class="photo outcome-photo" role="img" aria-label="Photo of a smiling patient in a yellow shirt being fitted with an arm prosthesis"></div>
    <div class="outcome">
      <div class="heading-red">All of these combined allow us to provide the best possible patient outcome</div>
      <ul>
        <li><svg width="10" height="10" viewBox="0 0 12 12"><path d="M2 11V6a4 4 0 0 1 8 0M7 3l3 3 2-3" stroke="var(--red)" stroke-width="1.6" fill="none"/></svg>Free consultations.</li>
        <li><svg width="10" height="10" viewBox="0 0 12 12"><path d="M2 11V6a4 4 0 0 1 8 0M7 3l3 3 2-3" stroke="var(--red)" stroke-width="1.6" fill="none"/></svg>Same Day Prosthetic Fitting Available</li>
        <li><svg width="10" height="10" viewBox="0 0 12 12"><path d="M2 11V6a4 4 0 0 1 8 0M7 3l3 3 2-3" stroke="var(--red)" stroke-width="1.6" fill="none"/></svg>Most items covered by insurance</li>
        <li><svg width="10" height="10" viewBox="0 0 12 12"><path d="M2 11V6a4 4 0 0 1 8 0M7 3l3 3 2-3" stroke="var(--red)" stroke-width="1.6" fill="none"/></svg>We accept Medicare, Medicaid, and most private insurances.</li>
      </ul>
    </div>
    <svg class="wave" viewBox="0 0 280 560" preserveAspectRatio="none" aria-hidden="true">
      <path d="M0,480 Q150,430 280,330 L280,560 L0,560Z" fill="var(--paper-shade)"/>
      <path d="M0,466 Q150,416 280,316" stroke="var(--red)" stroke-width="6" fill="none"/>
      <path d="M0,473 Q150,423 280,323" stroke="var(--paper)" stroke-width="4" fill="none"/>
      <path d="M0,480 Q150,430 280,330" stroke="var(--blue)" stroke-width="6" fill="none"/>
    </svg>
    <div class="web inside-web"><i></i>www.kinetralimb.example</div>
  </article>
</section>

</body>
</html>
```